Web Design for an Online Dating Web Site

We need an uncoded web design for a new online dating web site called pLirvo.com. Simplicity and boldness are the key factors in the successful design.
Please look at the requirements document attached for details.
Updates
Dear all,
Please AVOID USING A PICTURE OF A HAPPY COUPLE ON THE HOME PAGE of the site. We highly want to move away from this space as it makes our web site just like another dating web site.
We like something simple with web 2.0 look and feel. The examples in the Requirements Document are exactly the design we are after.
Regards
Tarn
Industry/Entity Type
Dating
Look and feel
Each slider illustrates characteristics of the customer's brand and the style your logo design should communicate.

```html
<!DOCTYPE html>
<html lang="en">
<head>
<meta charset="utf-8">
<title>pLirvo – Home</title>
<link href="https://fonts.googleapis.com/css2?family=Didact+Gothic&family=Arimo:wght@400;700&display=swap" rel="stylesheet">
<style>
:root{
  --teal-deep:#0a6676;
  --teal-mid:#2590a0;
  --teal-light:#3ba8b7;
  --band:#0f6e7d;
  --lime:#bbdf10;
  --lime-light:#e4f47a;
  --lime-dark:#8fb000;
  --pink:#e0288f;
  --pink-light:#ef6ab3;
  --ink:#1a1a1a;
  --white:#ffffff;
}
*{margin:0;padding:0;box-sizing:border-box}
html,body{width:1200px;height:1118px;overflow:hidden}
body{font-family:"Arimo",Arial,sans-serif;color:var(--white);background:var(--teal-light)}
.page{position:relative;width:1200px;height:1118px;overflow:hidden}
.hero{position:absolute;left:0;top:0;width:1200px;height:872px;
  background:linear-gradient(180deg,var(--teal-deep) 0%,#157d8d 22%,var(--teal-mid) 40%,var(--teal-light) 62%,var(--teal-light) 100%)}
.hero-pattern{position:absolute;inset:0;background:radial-gradient(ellipse at 12% 25%,rgba(10,90,105,.35),transparent 45%),radial-gradient(ellipse at 88% 25%,rgba(10,90,105,.35),transparent 45%)}
.stage-arc{position:absolute;left:100px;top:422px;width:1000px;height:560px;border-radius:50%;
  background:linear-gradient(180deg,rgba(90,190,205,.35),rgba(60,168,183,0) 40%)}
.brand{position:absolute;left:0;width:1200px;top:22px;text-align:center;font-family:"Arimo",sans-serif;font-weight:700;font-size:64px;color:var(--pink);letter-spacing:-1px}
.brand .mark{display:inline-block;width:26px;height:26px;border-radius:50%;background:var(--pink);margin-left:8px;vertical-align:middle}
.nav{position:absolute;left:141px;top:135px;width:919px;height:46px;border-radius:6px;
  background:linear-gradient(180deg,var(--lime-light) 0%,#d1ec3a 45%,var(--lime) 50%,var(--lime) 100%);
  box-shadow:0 3px 5px rgba(0,0,0,.3);display:flex;overflow:hidden}
.nav a{display:flex;align-items:center;justify-content:center;height:46px;font-weight:700;font-size:16px;color:var(--ink);text-decoration:none;border-right:1px solid rgba(140,170,0,.6)}
.nav a.active{background:linear-gradient(180deg,var(--pink-light) 0%,#e64aa2 45%,var(--pink) 50%,var(--pink) 100%);color:var(--white);text-shadow:0 1px 1px rgba(0,0,0,.4)}
.intro{position:absolute;left:258px;top:232px;width:652px}
.intro h1{font-family:"Didact Gothic",sans-serif;font-weight:400;font-size:41px;letter-spacing:-1px;white-space:nowrap}
.intro p{margin-top:16px;font-size:11.5px;line-height:15.5px}
.btn-signup{position:absolute;left:718px;top:349px;width:191px;height:52px;border-radius:12px;border:4px solid #a6d21a;
  background:linear-gradient(180deg,#f1fa9a 0%,#d9ef3e 45%,var(--lime) 100%);color:var(--ink);
  font-size:24px;display:flex;align-items:center;justify-content:center;box-shadow:inset 0 0 0 2px #f4fbb8}
.screenshot{position:absolute;left:418px;top:480px}
.dots{position:absolute;top:838px;left:0;width:1200px;height:12px}
.dots span{position:absolute;width:11px;height:11px;border-radius:50%;background:#1b7484}
.dots span.on{background:var(--lime)}
.login{position:absolute;left:0;top:872px;width:1200px;height:106px;background:var(--band);border-top:1px solid #1a8595}
.field{position:absolute;top:33px;height:42px;border:2px solid #3b96a4;border-radius:7px;background:#0c6a79;
  color:#cfe9ee;font-size:14px;padding:11px 0 0 18px;box-shadow:inset 0 1px 3px rgba(0,0,0,.35)}
.btn-login{position:absolute;left:581px;top:32px;width:117px;height:44px;border-radius:7px;
  background:linear-gradient(180deg,#f1fa9a 0%,#d9ef3e 45%,var(--lime) 100%);color:var(--ink);
  font-size:19px;display:flex;align-items:center;justify-content:center;box-shadow:0 2px 3px rgba(0,0,0,.35)}
.or{position:absolute;left:713px;top:45px;font-size:17px;color:#e6f3f5}
.net{position:absolute;width:30px;height:30px;border-radius:5px;box-shadow:0 1px 2px rgba(0,0,0,.3)}
.btn-more{position:absolute;left:977px;top:41px;width:78px;height:29px;border-radius:4px;
  background:linear-gradient(180deg,#eef98e,var(--lime));color:var(--ink);font-size:13px;padding:8px 0 0 15px}
.btn-more i{position:absolute;right:12px;top:9px;width:11px;height:11px;border-radius:50%;background:var(--white);border:1px solid #777}
.footer{position:absolute;left:0;top:978px;width:1200px;height:140px;background:var(--lime);color:var(--ink)}
.footer-brand{position:absolute;left:145px;top:22px;font-weight:700;font-size:40px;color:#5d7d06;letter-spacing:-1px}
.footer-brand .mark{display:inline-block;width:16px;height:16px;border-radius:50%;background:#5d7d06;margin-left:5px;vertical-align:middle}
.footer .rule{position:absolute;left:141px;top:92px;width:918px;height:1px;background:#a5c60a;border-bottom:1px solid #cfe94e}
.copyright{position:absolute;left:143px;top:108px;font-size:10px}
.footer-links{position:absolute;right:141px;top:109px;display:flex;gap:17px;font-size:10px}
.footer-links a{color:var(--ink);text-decoration:none}
</style>
</head>
<body>
<div class="page">
  <section class="hero">
    <div class="hero-pattern" role="img" aria-label="Soft swirling leaf ornament in darker teal"></div>
    <div class="stage-arc"></div>
    <div class="brand">pLirvo<span class="mark"></span></div>
    <nav class="nav">
      <a class="active" href="#" style="width:93px">Home</a>
      <a href="#" style="width:81px">Why</a>
      <a href="#" style="width:147px">How It Works</a>
      <a href="#" style="width:104px">Sign Up</a>
      <a href="#" style="width:118px">Our Blog</a>
    </nav>
    <div class="intro">
      <h1>Lorem ipsum dolor sit amet consecutor</h1>
      <p>Lorem ipsum dolor sit amet consecutor. Lorem ipsum dolor sit amet consecutor. Lorem ipsum dolor sit amet consecutor. Lorem ipsum dolor sit amet consecutor. Lorem ipsum dolor sit amet consecutor. Lorem ipsum dolor sit amet consecutor. Lorem ipsum dolor sit amet consecutor.</p>
    </div>
    <div class="btn-signup">Sign Up</div>
    <svg class="screenshot" width="400" height="330" viewBox="0 0 400 330" role="img" aria-label="Product screenshot area">
      <defs>
        <linearGradient id="reflect" x1="0" y1="0" x2="0" y2="1">
          <stop offset="0" stop-color="#2a95a4" stop-opacity=".7"/>
          <stop offset="1" stop-color="#3ba8b7" stop-opacity="0"/>
        </linearGradient>
      </defs>
      <polygon points="7,6 80,16 80,270 4,270" fill="#1d8595"/>
          <polygon points="80,6 390,61 388,270 80,270" fill="#1e8797"/>
      <rect x="4" y="270" width="384" height="60" fill="url(#reflect)"/>
      <text x="234" y="184" text-anchor="middle" font-family="Arimo, sans-serif" font-size="33" fill="#7cc3cd" transform="rotate(3 234 184)">Screenshot</text>
    </svg>
    <div class="dots">
      <span class="on" style="left:543px"></span>
      <span style="left:566px"></span>
      <span style="left:591px"></span>
      <span style="left:617px"></span>
      <span style="left:641px"></span>
    </div>
  </section>

  <section class="login">
    <div class="field" style="left:144px;width:206px">Email Address</div>
    <div class="field" style="left:364px;width:204px">Password</div>
    <div class="btn-login">Login</div>
    <div class="or">OR</div>
    <span class="net" style="left:755px;top:40px;background:#3b5a9a" aria-label="Network login"></span>
    <span class="net" style="left:799px;top:40px;background:#e9e9e9" aria-label="Network login"></span>
    <span class="net" style="left:844px;top:40px;background:#6d2c7c" aria-label="Network login"></span>
    <span class="net" style="left:888px;top:40px;background:#dcdcdc" aria-label="Network login"></span>
    <span class="net" style="left:932px;top:40px;background:#1e5cb5" aria-label="Network login"></span>
    <div class="btn-more">More<i></i></div>
  </section>

  <footer class="footer">
    <div class="footer-brand">pLirvo<span class="mark"></span></div>
    <span class="net" style="left:793px;top:37px;background:#3b5a9a"></span>
    <span class="net" style="left:832px;top:37px;background:#44a9d8"></span>
    <span class="net" style="left:872px;top:37px;background:#2f8d45"></span>
    <span class="net" style="left:911px;top:37px;background:#1e5cb5"></span>
    <span class="net" style="left:950px;top:37px;background:#6d2c7c"></span>
    <span class="net" style="left:990px;top:37px;background:#e9e9e9"></span>
    <span class="net" style="left:1029px;top:37px;background:#f2f2f2"></span>
    <div class="rule"></div>
    <div class="copyright">© 2011 pLirvo. All Rights Reserved</div>
    <div class="footer-links">
      <a href="#">Home</a><a href="#">Why</a><a href="#">How It Works</a><a href="#">Sign Up</a><a href="#">Our Blog</a>
    </div>
  </footer>
</div>
</body>
</html>
```